Green Logistics / Last Mile Delivery Firm needs cool one-page website

FYI - We do have a detailed brief in the uploaded files section below
COMPANY
We recently launched the company Quillby Logistics which is a pioneer in urban green logistics and provides zero-emissions last mile delivery services (i.e. delivery of parcels with delivery vans to the doorstep of households) for its logistics and retail clients.
We take on urban parcel delivery for our clients with a 100% electric commercial vehicles fleet, fair and sustainable working conditions for our employees and an unparalleled professional and customer-focused mindset.
WEBSITE
In the detailed brief, we have provided examples to emulate. We need the design + coding of the website. Website needs to be friendly/optimized for and should open swiftly on both Android & iOS.
In general, the website should convey
- green mission of the company
- sustainability (good working conditions, focus on employees)
- customer orientation
- professionalism
DESIGN
In the detailed brief, we have provided designs to emulate.
Color design: we do have a logo which features 2 green colors (one lighter and one darker color tone). However, the colors on the website do not necessarily need to follow these 2 colors exactly as we are able to switch the logo colors.
Imagery: should reflect maybe 50% green/leaf/tree , 25% customer and employee orientation, and 25% logistics (here it's important that it is the last mile delivery, i.e. delivery with delivery vans to the doorstep of households)

```html
<!DOCTYPE html>
<html lang="en">
<head>
<meta charset="utf-8">
<title>Quillby Logistics</title>
<link href="https://fonts.googleapis.com/css2?family=Poppins:wght@300;400;500;600;700&display=swap" rel="stylesheet">
<style>
:root{
  --green:#1e9b4a;
  --green-dark:#16873e;
  --lime:#8cc63f;
  --ink:#222;
  --text:#444;
  --muted:#777;
  --line:#d9d9d9;
  --gold:#d4ae4c;
  --footer:#232323;
  --white:#fff;
}
*{box-sizing:border-box;margin:0;padding:0}
html,body{width:1200px;height:5076px;overflow:hidden}
body{position:relative;font-family:'Poppins',sans-serif;color:var(--text);background:var(--white)}
.abs{position:absolute}
.center{text-align:center}

/* hero */
.hero{position:absolute;left:0;top:0;width:1200px;height:743px;background:linear-gradient(180deg,#3c5a3a 0%,#5b7f45 35%,#4d6f3b 60%,#2f3b33 100%)}
.hero-shade{position:absolute;inset:0;background:rgba(0,0,0,.28)}
.topbar{position:absolute;left:0;top:0;width:1200px;height:70px;font-size:13px;color:var(--lime)}
.topbar .item{position:absolute;top:38px;display:flex;align-items:center;gap:8px}
.brand{position:absolute;left:36px;top:106px;display:flex;align-items:center;gap:12px}
.brand .dot{width:60px;height:60px;border-radius:50%;background:var(--lime)}
.brand .name{font-size:26px;font-weight:600;color:var(--lime);letter-spacing:.5px}
.nav{position:absolute;left:532px;top:132px;display:flex;gap:22px;font-size:15px;font-weight:500;color:var(--white)}
.lang{position:absolute;left:960px;top:130px;width:178px;height:36px;background:var(--green);color:var(--white);font-size:12px;font-weight:600;display:flex;align-items:center;justify-content:center;gap:6px;border-radius:2px}
.hero h1{position:absolute;left:0;width:1200px;top:314px;font-size:50px;font-weight:600;color:var(--white);text-align:center;letter-spacing:1px}
.hero h1 span{color:var(--green)}
.hero p{position:absolute;left:220px;width:760px;top:430px;font-size:21px;line-height:41px;color:var(--white);text-align:center}
.btn-hero{position:absolute;left:491px;top:564px;width:218px;height:54px;border-radius:27px;background:var(--green);color:var(--white);font-size:16px;font-weight:500;display:flex;align-items:center;justify-content:center;gap:10px}

/* about */
.section-title{position:absolute;left:0;width:1200px;text-align:center;font-weight:600;font-size:33px}
.section-title.dark{color:var(--ink)}
.section-title.green{color:var(--green);text-transform:uppercase}
.dots{position:absolute;height:0;border-top:3px dotted var(--green)}
.about-col{position:absolute;top:872px;width:300px;text-align:center}
.about-col h3{font-size:22px;font-weight:500;color:var(--green);margin-bottom:20px}
.about-col p{font-size:12px;line-height:23px;color:var(--text)}
.btn-outline{position:absolute;height:40px;border:2px solid var(--green);color:var(--green);font-size:11px;font-weight:500;display:flex;align-items:center;justify-content:center;text-transform:uppercase;background:var(--white)}

/* band */
.band{position:absolute;left:0;top:1176px;width:1200px;height:327px;background:var(--lime)}
.band-col{position:absolute;top:1268px;width:310px;text-align:center;color:var(--white)}
.band-col h3{font-size:22px;font-weight:500;margin-bottom:16px}
.band-col p{font-size:12px;line-height:23px;color:#eef6e2}

/* intro */
.intro-title{position:absolute;left:160px;top:1578px;font-size:34px;font-weight:600;color:var(--green)}
.intro-text{position:absolute;left:160px;top:1676px;width:330px;font-size:12.5px;line-height:23.5px;color:var(--green)}
.photo{position:absolute}

/* services */
.lead{position:absolute;left:240px;width:720px;text-align:center;font-size:12.5px;line-height:23px;color:var(--gold)}
.card{position:absolute;top:2179px;height:330px;background:var(--white);border-radius:22px 22px 14px 14px;box-shadow:0 4px 14px rgba(0,0,0,.16);border-bottom:5px solid var(--green);padding:72px 32px 0}
.card h3{font-size:21px;line-height:25px;font-weight:600;color:var(--green)}
.card .rule{height:3px;background:#bfe3c4;margin:12px -32px 30px}
.card p{font-size:12px;line-height:24px;color:var(--lime)}
.btn-pill{position:absolute;left:32px;width:148px;height:40px;border-radius:20px;background:var(--green);color:var(--white);font-size:12px;font-weight:600;display:flex;align-items:center;justify-content:center}

/* touch */
.touch{position:absolute;left:0;top:2650px;width:1200px;height:285px;background:linear-gradient(90deg,#2a2420,#4a3b31 50%,#2c2622)}
.touch-text{position:absolute;left:136px;top:2760px;width:540px;font-size:13px;line-height:23px;color:var(--gold)}
.btn-gold{position:absolute;left:932px;top:2778px;width:158px;height:40px;border:2px solid var(--green);color:var(--green);font-size:12px;display:flex;align-items:center;justify-content:center;text-transform:uppercase}

/* careers */
.careers-text{position:absolute;left:106px;top:3186px;width:420px;font-size:12.5px;line-height:19.5px;color:var(--ink)}
.acc{position:absolute;left:573px;width:460px;border-top:1px solid var(--line)}
.acc-head{position:absolute;left:593px;font-size:12px;font-weight:600;color:var(--green)}
.acc-list{position:absolute;left:593px;top:3140px;width:440px;font-size:11.5px;line-height:23px;color:var(--green)}

/* contact */
.map{position:absolute;left:0;top:3733px;width:1200px;height:351px;background:linear-gradient(135deg,#e8eddf,#dfe6d6 45%,#e9e4d6)}
.info{position:absolute;top:4130px;width:300px;text-align:center}
.info .label{font-size:18px;color:var(--green);margin-top:18px}
.info .value{font-size:18px;color:var(--green);margin-top:20px}
.field{position:absolute;border:1px solid #ccc;font-size:12px;color:#777;padding:8px 12px;background:var(--white)}
.btn-send{position:absolute;left:522px;top:4557px;width:150px;height:43px;background:#21c06b;color:var(--white);font-size:14px;display:flex;align-items:center;justify-content:center}

/* footer */
.footer{position:absolute;left:0;top:4639px;width:1200px;height:437px;background:var(--footer)}
.f-dot{position:absolute;left:557px;top:4672px;width:86px;height:86px;border-radius:50%;background:var(--lime)}
.f-name{position:absolute;left:0;width:1200px;top:4786px;text-align:center;font-size:32px;font-weight:600;color:var(--lime)}
.social{position:absolute;top:4844px;width:36px;height:36px;border-radius:50%;background:var(--lime)}
.legal{position:absolute;left:0;width:1200px;top:4896px;text-align:center;font-size:22px;font-weight:600;color:var(--lime)}
.legal-text{position:absolute;left:0;width:1200px;top:4950px;text-align:center;font-size:13px;color:var(--lime)}
.f-nav{position:absolute;left:0;width:1200px;top:4998px;display:flex;justify-content:center;gap:36px;font-size:17px;font-weight:600;color:var(--white)}
.copy{position:absolute;left:0;width:1200px;top:5044px;text-align:center;font-size:14px;color:var(--white)}
</style>
</head>
<body>

<header class="hero" role="img" aria-label="Aerial photo of a straight highway through green fields at dusk">
  <div class="hero-shade"></div>
</header>
<div class="topbar">
  <div class="item" style="left:790px">
    <svg width="20" height="16" viewBox="0 0 20 16"><rect x="1" y="1" width="18" height="14" rx="2" fill="none" stroke="#8cc63f" stroke-width="1.6"/><path d="M1 2l9 7 9-7" fill="none" stroke="#8cc63f" stroke-width="1.6"/></svg>
    hello@quillbylogistics.com
  </div>
  <div class="item" style="left:1014px">
    <svg width="16" height="16" viewBox="0 0 24 24"><path d="M6.6 10.8a15.2 15.2 0 006.6 6.6l2.2-2.2a1 1 0 011-.25 11.4 11.4 0 003.6.57 1 1 0 011 1V20a1 1 0 01-1 1A17 17 0 013 4a1 1 0 011-1h3.5a1 1 0 011 1c0 1.25.2 2.45.57 3.57a1 1 0 01-.25 1z" fill="#8cc63f"/></svg>
    +31 500 123 456
  </div>
</div>
<div class="brand"><span class="dot"></span><span class="name">QUILLBY LOGISTICS</span></div>
<nav class="nav"><span>Home</span><span>About</span><span>Services</span><span>Careers</span><span>Contact</span></nav>
<div class="lang">SELECT LANGUAGE <svg width="10" height="8" viewBox="0 0 10 8"><path d="M1 2l4 4 4-4" stroke="#fff" stroke-width="2" fill="none"/></svg></div>
<h1 class="hero-title" style="position:absolute;left:0;width:1200px;top:314px;font-size:50px;font-weight:600;color:#fff;text-align:center;letter-spacing:1px"><span style="color:var(--green)">QUILLBY</span> LOGISTICS</h1>
<p style="position:absolute;left:220px;width:760px;top:430px;font-size:21px;line-height:41px;color:#fff;text-align:center">Quillby Logistics provides last mile delivery services in urban areas to clients in the logistics and retail space</p>
<div class="btn-hero">GET STARTED <svg width="18" height="14" viewBox="0 0 18 14"><path d="M1 7h15M10 1l6 6-6 6" stroke="#fff" stroke-width="2" fill="none"/></svg></div>

<section class="about">
  <h2 class="section-title dark" style="top:786px">ABOUT US</h2>
  <div class="about-col" style="left:122px"><h3>Who we are</h3><p>Quillby Logistics is a pioneer in urban green logistics and provides zeroemissions last mile delivery services for its logistics and retail clients.</p></div>
  <div class="about-col" style="left:449px"><h3>Our Mission</h3><p>To satisfy consumers' ever-rising desire to buy products online, the CO2 emissions from delivery traffic will increase by 32% in the top 100 cities globally until 2030.</p></div>
  <div class="about-col" style="left:778px"><h3>Our values</h3><p>We see ourselves as a professional services company who strongly cares about the environment, its clients and their customers, as well as its employees.</p></div>
  <div class="btn-outline" style="left:194px;top:1060px;width:156px">Learn More</div>
  <div class="btn-outline" style="left:522px;top:1063px;width:156px">Learn More</div>
  <div class="btn-outline" style="left:850px;top:1060px;width:156px">Learn More</div>
</section>

<section>
  <div class="band"></div>
  <svg class="abs" style="left:0;top:1176px" width="1200" height="90" viewBox="0 0 1200 90"><polygon points="0,0 1200,0 1200,86 0,16" fill="#1e9b4a"/></svg>
  <div class="band-col" style="left:117px"><h3>Green Logistics</h3><p>Voluptatum deleniti atque corrupti quos dolores et quas molestias excepturi sint occaecati cupiditate non provident</p></div>
  <div class="band-col" style="left:445px"><h3>Green Last Mile</h3><p>Voluptatum deleniti atque corrupti quos dolores et quas molestias excepturi sint occaecati cupiditate non provident</p></div>
  <div class="band-col" style="left:773px"><h3>Sustainable Last Mile</h3><p>Voluptatum deleniti atque corrupti quos dolores et quas molestias excepturi sint occaecati cupiditate non provident</p></div>
</section>

<section>
  <h2 class="intro-title">QUILLBY LOGISTICS</h2>
  <div class="dots" style="left:160px;top:1632px;width:250px"></div>
  <p class="intro-text">We Recently Launched The Company Quillby Logistics Which Is A Pioneer In Urban Green Logistics And Provides Zero-Emissions Last Mile Delivery Services (I.E. Delivery Of Parcels With Delivery Vans To The Doorstep Of Households) For Its Logistics And Retail Clients.</p>
  <div class="btn-outline" style="left:160px;top:1846px;width:150px">Read More</div>
  <div class="photo" role="img" aria-label="Truck on a highway at sunset beside a truck shape made of green leaves" style="left:492px;top:1531px;width:598px;height:410px;background:linear-gradient(180deg,#7b7a72 0%,#c9b48a 30%,#9a9a92 55%,#5f655c 100%)"></div>
  <div class="photo" role="img" aria-label="Leafy green truck shape" style="left:492px;top:1760px;width:260px;height:160px;background:radial-gradient(ellipse at center,#4f9a2e 0%,#3c7d24 60%,rgba(60,125,36,0) 72%)"></div>
</section>

<section>
  <h2 class="section-title green" style="top:1976px">Our Services</h2>
  <div class="dots" style="left:515px;top:2027px;width:170px"></div>
  <p class="lead" style="top:2056px">Quillby Logistics Provides Last Mile Delivery Services In Urban Areas To Clients In The Logistics And Retail Space. Our Permanent Employees Are All Highly Trained And Commit To Highest Professional Standards Which We Continuously Review And Further Develop With Them.</p>
  <article class="card" style="left:32px;width:273px"><h3>Highly trained delivery drivers</h3><div class="rule"></div><p>We only employ permanently, train far above average, and live a great team spirit</p><div class="btn-pill" style="top:240px">READ MORE</div></article>
  <article class="card" style="left:315px;width:284px"><h3>Zero-emission delivery</h3><div class="rule"></div><p>We operate a 100% electric commercial vehicle fleet.lorem ipsum is here.</p><div class="btn-pill" style="top:240px">READ MORE</div></article>
  <article class="card" style="left:611px;width:273px"><h3>Professional all around</h3><div class="rule"></div><p>We honor our commitments and hold ourselves to the highest professional standards</p><div class="btn-pill" style="top:263px">READ MORE</div></article>
  <article class="card" style="left:894px;width:274px"><h3>Professional all around</h3><div class="rule"></div><p>We honor our commitments and hold ourselves to the highest professional standards</p><div class="btn-pill" style="top:263px">READ MORE</div></article>
</section>

<section>
  <h2 class="section-title green" style="top:2559px">Get In Touch With Quillby Logistics</h2>
  <div class="dots" style="left:325px;top:2612px;width:550px"></div>
  <div class="touch" role="img" aria-label="Group of people stretching together on a wooden deck"></div>
  <p class="touch-text">If You Got Excited, Or Have A Question About Our Services, Our Approach, Our Jobs Or Just Want To Get In Touch To Chat About How Green Logistics Can Make The Planet A Little Bit Better, Please Get In Touch!</p>
  <div class="btn-gold">Contact Us</div>
</section>

<section>
  <h2 class="section-title green" style="top:2959px">Careers</h2>
  <div class="dots" style="left:540px;top:3014px;width:120px"></div>
  <p class="careers-text">If You Join Quillby Logistics, You Join A Family. We Elevate One Another, Care For Each Other's Wellbeing And Growth, And Celebrate Our Successes. We Strongly Believe Growth Is A Team Sport And That Every Member Of The Family Fully Contributes To The Achievements Of The Company Overall. At The Heart Of Everything We Do At Quillby Logistics Is A Relentless Focus On Our Mission. That's Why We Aim To Ensure Our Employees Can Follow Their Own Passion At The Workplace, Be This Working In A Truly Collaborative And Caring Team, Putting A Smile On A Customer's Face Or Making The World A Better Place.</p>
  <div class="btn-outline" style="left:106px;top:3410px;width:150px">Read More</div>

  <div class="acc" style="top:3060px"></div>
  <div class="acc-head" style="top:3092px">&#8212;&nbsp; Your tasks as a delivery driver:</div>
  <div class="acc-list">
    – Delivery of packages to end customers<br>
    – In the delivery center: preparation of the tour and loading of the delivery van with parcels<br>
    – Drive from the delivery center to the delivery area – you will be guided by a navigation system<br>
    – Delivery of the parcels to end customers in the delivery area – the navigation helps you here too<br>
    – Suggest ideas for improvement in the delivery process<br>
    – Take care of and charge the delivery van
  </div>
  <div class="acc" style="top:3400px"></div>
  <div class="acc-head" style="top:3435px">+&nbsp; Required knowledge and skills:</div>
  <div class="acc" style="top:3487px"></div>
  <div class="acc-head" style="top:3519px">+&nbsp; What you can expected from the Quillby Logistics family:</div>
  <div class="acc" style="top:3570px"></div>
</section>

<section>
  <h2 class="section-title green" style="top:3619px">Contact</h2>
  <div class="dots" style="left:540px;top:3672px;width:120px"></div>
  <p class="abs center" style="left:0;width:1200px;top:3686px;font-size:13px;color:var(--green)">We'd Love To Hear From You!</p>
  <div class="map" role="img" aria-label="Street map of the greater city area with a location pin"></div>

  <div class="info" style="left:116px">
    <svg width="40" height="40" viewBox="0 0 24 24"><path d="M21 3L3 10.5l7.5 3 3 7.5z" fill="none" stroke="#1e9b4a" stroke-width="1.4" stroke-linejoin="round"/></svg>
    <div class="label">Location</div><div class="value">A108 Linden Street, Springfield</div>
  </div>
  <div class="info" style="left:449px">
    <svg width="40" height="40" viewBox="0 0 24 24"><path d="M6.6 10.8a15.2 15.2 0 006.6 6.6l2.2-2.2a1 1 0 011-.25 11.4 11.4 0 003.6.57 1 1 0 011 1V20a1 1 0 01-1 1A17 17 0 013 4a1 1 0 011-1h3.5a1 1 0 011 1c0 1.25.2 2.45.57 3.57a1 1 0 01-.25 1z" fill="#1e9b4a"/></svg>
    <div class="label">Phone</div><div class="value">+(12) 555 0148</div>
  </div>
  <div class="info" style="left:782px">
    <svg width="40" height="40" viewBox="0 0 24 24"><rect x="3" y="6" width="18" height="14" fill="none" stroke="#1e9b4a" stroke-width="1.4"/><path d="M3 6l9 8 9-8" fill="none" stroke="#1e9b4a" stroke-width="1.4"/><path d="M7 6V3h10v3" fill="none" stroke="#1e9b4a" stroke-width="1.4"/></svg>
    <div class="label">@Email</div><div class="value">info@quillby.example</div>
  </div>

  <div class="field" style="left:134px;top:4320px;width:458px;height:34px">Your Name</div>
  <div class="field" style="left:607px;top:4320px;width:457px;height:34px">Your Email</div>
  <div class="field" style="left:134px;top:4370px;width:930px;height:32px">Subject</div>
  <div class="field" style="left:134px;top:4419px;width:930px;height:123px">Message</div>
  <div class="btn-send">Send Message</div>
</section>

<footer>
  <div class="footer"></div>
  <div class="f-dot"></div>
  <div class="f-name">QUILLBY LOGISTICS</div>
  <span class="social" style="left:532px"></span>
  <span class="social" style="left:582px"></span>
  <span class="social" style="left:632px"></span>
  <div class="legal">Legal Notice</div>
  <div class="legal-text">Et Aut Eum Quis Fuga Eos Sunt Ipsa Nihil. Labore Corporis Magni Eligendi Fuga Maxime Saepe Commodi Placeat.</div>
  <nav class="f-nav"><span>HOME</span><span>ABOUT</span><span>SERVICES</span><span>CAREERS</span><span>CONTACT</span></nav>
  <div class="copy">© 2020 Quillby Logistics All Rights Reserved</div>
</footer>

</body>
</html>
```